PostCard for Managed IT Services

We need a postcard design for a postcard that we intend to send out early in our marketing efforts to medical practices. The postcard should communicate our core services for small businesses including 1.) Managed IT Services, 2.) Security Services, 3.) Cloud Services, and 4.) IT Project and Integration work. company information is available at www.ferndaleit.com. I attached a two logos.WHILE WE WANT TO USE THE LOGO AND COLORS FROM OUR SITE, I HOPE THE DESIGN IS BOLD AND GRABS ATTENTION. I HOPE IT IS NOT THE 'SAME OLD' INFORMATION TECHNOLOGY LOOK. BE CREATIVE AND GET THE READER TO LOOK TWICE.

Target Market(s)

Businesses, medical practices

Font styles to use
Serif
Sans Serif

Requirements
Must have
• We need to include somewhere that are technicians are trained in on HIPAA and PCI (see site for info on the two)

```html
<!DOCTYPE html>
<html lang="en">
<head>
<meta charset="utf-8">
<title>Ferndale Managed Services – Postcard</title>
<link href="https://fonts.googleapis.com/css2?family=Montserrat:ital,wght@0,400;0,500;0,600;0,700;0,800;1,600&display=swap" rel="stylesheet">
<style>
  :root {
    --blue: #2b3f9b;
    --blue-dark: #1f2f80;
    --green: #3cb04a;
    --charcoal: #444547;
    --ink: #3a3a3c;
    --paper: #ffffff;
    --stage: #e4e5e3;
    --stamp: #e3e3e3;
    --rule: #e2e2e2;
    --photo-a: #c9d3d8;
    --photo-b: #6f8a99;
    --photo-c: #23506e;
  }
  * { box-sizing: border-box; margin: 0; padding: 0; }
  html, body { width: 1200px; height: 1200px; overflow: hidden; }
  body {
    background: var(--stage);
    font-family: "Montserrat", sans-serif;
    color: var(--ink);
    position: relative;
  }
  .postcard {
    position: absolute;
    left: 210px;
    width: 780px;
    height: 520px;
    background: var(--paper);
    overflow: hidden;
    box-shadow: 0 6px 18px rgba(0,0,0,.18);
  }
  .postcard--front { top: 45px; }
  .postcard--back { top: 635px; }
  .postcard__shapes { position: absolute; inset: 0; }

  /* Front */
  .brand {
    position: absolute; top: 26px; left: 455px; width: 240px;
    display: flex; align-items: center; justify-content: center; gap: 8px;
    font-weight: 700; font-size: 15px; color: var(--blue);
  }
  .brand__dot { width: 14px; height: 14px; border-radius: 50%; background: var(--blue); }
  .headline {
    position: absolute; top: 62px; left: 392px; width: 370px;
    text-align: center; color: var(--blue); font-weight: 800; line-height: .95;
  }
  .headline__top { display: block; font-size: 27px; letter-spacing: .5px; }
  .headline__main { display: block; font-size: 64px; letter-spacing: 1px; }
  .tagline {
    position: absolute; top: 166px; left: 410px; width: 334px;
    background: var(--green); color: #fff;
    font-size: 13px; font-weight: 600; font-style: italic;
    text-align: center; padding: 5px 0;
  }
  .services {
    position: absolute; top: 214px; left: 392px; width: 370px;
    display: flex; justify-content: space-between; list-style: none;
  }
  .service { width: 88px; text-align: center; font-size: 11.5px; font-weight: 500; line-height: 1.2; }
  .service__icon {
    width: 50px; height: 50px; margin: 0 auto 7px; border-radius: 50%;
    background: #eef0f6; display: flex; align-items: center; justify-content: center;
  }
  .compliance {
    position: absolute; top: 352px; left: 390px; width: 380px;
    text-align: center; font-size: 12px;
  }
  .compliance strong { font-size: 20px; font-weight: 700; color: var(--blue); }
  .band-call {
    position: absolute; left: 0; right: 0; top: 400px; height: 52px;
    color: #fff; font-size: 26px; font-weight: 500;
    display: flex; align-items: center; justify-content: flex-end; padding-right: 40px;
  }
  .band-call strong { font-weight: 700; margin-left: 12px; }
  .band-contact {
    position: absolute; left: 0; right: 0; top: 452px; height: 68px;
    color: #fff; font-size: 13px; font-weight: 500;
    display: flex; align-items: center; justify-content: flex-end; gap: 50px; padding-right: 40px;
  }
  .band-contact span { display: inline-flex; align-items: center; gap: 7px; }

  /* Back */
  .licensing {
    position: absolute; top: 38px; left: 0; width: 440px; height: 96px;
    padding: 14px 40px 0 34px;
    color: #fff; font-size: 12.5px; font-weight: 700; line-height: 1.4;
  }
  .intro {
    position: absolute; top: 152px; left: 34px; width: 380px;
    font-size: 12.5px; line-height: 1.45;
  }
  .intro p + p { margin-top: 6px; }
  .cta {
    position: absolute; top: 318px; left: 34px; width: 380px;
    font-size: 20px; font-weight: 700; line-height: 1.2; color: #222;
  }
  .postcard--back .band-call { justify-content: flex-start; padding-left: 40px; }
  .postcard--back .band-contact { justify-content: flex-start; padding-left: 40px; }
</style>
</head>
<body>

<section class="postcard postcard--front" aria-label="Postcard front">
  <svg class="postcard__shapes" width="780" height="520" viewBox="0 0 780 520">
    <defs>
      <linearGradient id="photoTone" x1="0" y1="0" x2="1" y2="1">
        <stop offset="0" stop-color="var(--photo-a)"/>
        <stop offset=".55" stop-color="var(--photo-b)"/>
        <stop offset="1" stop-color="var(--photo-c)"/>
      </linearGradient>
    </defs>
    <rect x="0" y="400" width="780" height="52" fill="var(--blue)"/>
    <rect x="0" y="452" width="780" height="68" fill="var(--charcoal)"/>
    <path d="M0 0 H235 C345 110 385 330 300 520 H0 Z" fill="url(#photoTone)" role="img" aria-label="Photo of a doctor typing on a laptop beside a tablet showing medical data"/>
    <path d="M235 0 C345 110 385 330 300 520" fill="none" stroke="var(--blue)" stroke-width="12"/>
  </svg>

  <div class="brand"><span class="brand__dot"></span>Ferndale IT</div>
  <h1 class="headline"><span class="headline__top">FERNDALE MANAGED</span><span class="headline__main">SERVICES</span></h1>
  <p class="tagline">Partner with the best for all your IT needs!</p>

  <ul class="services">
    <li class="service">
      <div class="service__icon"><svg width="28" height="28" viewBox="0 0 28 28" fill="none" stroke="var(--blue)" stroke-width="2"><rect x="3" y="5" width="22" height="14" rx="1"/><path d="M10 24h8M14 19v5"/></svg></div>
      Managed IT Services
    </li>
    <li class="service">
      <div class="service__icon"><svg width="28" height="28" viewBox="0 0 28 28" fill="none" stroke="var(--blue)" stroke-width="2"><path d="M14 3l9 4v6c0 6-4 10-9 12-5-2-9-6-9-12V7z"/><path d="M10 14l3 3 5-6"/></svg></div>
      Security Services
    </li>
    <li class="service">
      <div class="service__icon"><svg width="28" height="28" viewBox="0 0 28 28" fill="none" stroke="var(--blue)" stroke-width="2"><path d="M8 20h13a5 5 0 0 0 0-10 7 7 0 0 0-13-1 5.5 5.5 0 0 0 0 11z"/></svg></div>
      Cloud Services
    </li>
    <li class="service">
      <div class="service__icon"><svg width="28" height="28" viewBox="0 0 28 28" fill="none" stroke="var(--blue)" stroke-width="2"><path d="M4 18l6 6M10 24h10l4-4M4 18h9a2 2 0 0 1 0 4h-4"/><rect x="12" y="4" width="10" height="9" rx="1"/></svg></div>
      IT Project &amp; Integration work
    </li>
  </ul>

  <p class="compliance">Technicians are trained in on <strong>HIPAA and PCI</strong></p>

  <div class="band-call">Call Us <strong>(555) 014-2290</strong></div>
  <div class="band-contact">
    <span><svg width="12" height="12" viewBox="0 0 12 12"><circle cx="6" cy="6" r="5" fill="none" stroke="#fff" stroke-width="1.5"/><path d="M1 6h10M6 1c2 2 2 8 0 10M6 1c-2 2-2 8 0 10" fill="none" stroke="#fff" stroke-width="1"/></svg>www.ferndaleit.com</span>
    <span><svg width="13" height="10" viewBox="0 0 13 10"><rect x=".5" y=".5" width="12" height="9" fill="none" stroke="#fff"/><path d="M.5 .5l6 5 6-5" fill="none" stroke="#fff"/></svg>info@ferndaleit.com</span>
  </div>
</section>

<section class="postcard postcard--back" aria-label="Postcard back">
  <svg class="postcard__shapes" width="780" height="520" viewBox="0 0 780 520">
    <rect x="0" y="38" width="460" height="96" fill="var(--green)"/>
    <rect x="0" y="400" width="780" height="52" fill="var(--blue)"/>
    <rect x="0" y="452" width="780" height="68" fill="var(--charcoal)"/>
    <path d="M430 0 C430 250 520 460 660 520 H780 V0 Z" fill="var(--paper)"/>
    <path d="M430 0 C430 250 520 460 660 520" fill="none" stroke="var(--blue)" stroke-width="10"/>
    <rect x="655" y="48" width="92" height="92" rx="12" fill="var(--stamp)"/>
    <g stroke="var(--rule)" stroke-width="1.5">
      <line x1="500" y1="200" x2="745" y2="200"/>
      <line x1="510" y1="240" x2="745" y2="240"/>
      <line x1="525" y1="280" x2="745" y2="280"/>
      <line x1="545" y1="320" x2="745" y2="320"/>
    </g>
  </svg>

  <p class="licensing">We are Nimbus Software partners and we sell volume licensing and software assurance. Please give us a call, (555) 014-2290 if you need a quote on Nimbus Software’s Volume Licensing!</p>

  <div class="intro">
    <p>Welcome to Ferndale Managed Services! We are committed to being the leading Managed IT Service Provider. We are located in Riverton, ND and we serve clients nationwide! We have and serve clients in every industry. Your data and network need to be secure in today’s world and we do our best to ensure that it is.</p>
    <p>At Ferndale IT, our goal is to provide the best IT solution for your business while keeping your IT costs down.</p>
  </div>

  <p class="cta">Contact us today to find out how we can serve your business!</p>

  <div class="band-call">Call Us <strong>(555) 014-2290</strong></div>
  <div class="band-contact">
    <span><svg width="12" height="12" viewBox="0 0 12 12"><circle cx="6" cy="6" r="5" fill="none" stroke="#fff" stroke-width="1.5"/><path d="M1 6h10M6 1c2 2 2 8 0 10M6 1c-2 2-2 8 0 10" fill="none" stroke="#fff" stroke-width="1"/></svg>www.ferndaleit.com</span>
    <span><svg width="13" height="10" viewBox="0 0 13 10"><rect x=".5" y=".5" width="12" height="9" fill="none" stroke="#fff"/><path d="M.5 .5l6 5 6-5" fill="none" stroke="#fff"/></svg>info@ferndaleit.com</span>
  </div>
</section>

</body>
</html>
```